Health Coach needs a Business Card Design

Need a really modern feminine business card design for a health and lifestyle coach. Needs to use geometric shapes, muted grey/blue/green pastels and black and white - see mood board attached and logo. The client likes black and white, modern, san serif with the use of lines and possibly a shadow leaf as in the mood board. Possibly put the tag line on the back or an icon of the logo. Logo is also attached. An icon of the logo would be great too.

Target Market(s)

Women (some men) aged 30 to 50.

Industry/Entity Type

Business

Contact Information for Business Card

Marla Teveny
e-mail: hello@marlatwell.example
website: marlatwell.example
Phone: +610497258316

The tag line is "Calm strength every day"

Font styles to use
Sans Serif

Colors
ecf7fb
cfeae6
000000
ffffff
f5f5f5

Requirements
Must have
• Black and white, logo, tag line and details
Nice to have
• Would be nice to incorporate the shadow palm.fern leaves as in the mood board and or geometric lines/shapes - see mood board. Could be either standard rectangle or would be happy with square too.
Should not have
• Flowers or decorations

```html
<!DOCTYPE html>
<html lang="en">
<head>
<meta charset="utf-8">
<title>Marla T — Business Card</title>
<link rel="stylesheet" href="https://fonts.googleapis.com/css2?family=Heebo:wght@300;400&display=swap">
<style>
  :root {
    --stage: #161616;
    --card: #000000;
    --brand-grey: #a2a2a2;
    --tagline-grey: #8c8c8c;
    --name-grey: #b9b9b9;
    --detail-grey: #a8a8a8;
  }
  * { margin: 0; padding: 0; box-sizing: border-box; }
  html, body {
    width: 1200px;
    height: 741px;
    overflow: hidden;
    background: var(--stage);
    font-family: "Heebo", sans-serif;
  }
  .canvas {
    position: relative;
    width: 1200px;
    height: 741px;
  }
  .card {
    position: absolute;
    top: 229px;
    width: 494px;
    height: 282px;
    background: var(--card);
    text-align: center;
  }
  .card--front { left: 100px; }
  .card--back  { left: 607px; }

  .brand-name {
    position: absolute;
    left: 0; right: 0;
    font-weight: 300;
    font-size: 27px;
    letter-spacing: 2px;
    color: var(--brand-grey);
    line-height: 1;
  }
  .tagline {
    position: absolute;
    left: 0; right: 0;
    font-weight: 400;
    font-size: 9.5px;
    letter-spacing: 4.2px;
    color: var(--tagline-grey);
    line-height: 1;
  }
  .card--front .brand-name { top: 120px; }
  .card--front .tagline    { top: 162px; padding-left: 44px; }

  .card--back .brand-name { top: 59px; }
  .card--back .tagline    { top: 102px; }

  .person-name {
    position: absolute;
    left: 0; right: 0;
    top: 148px;
    font-weight: 400;
    font-size: 16px;
    letter-spacing: 1.4px;
    color: var(--name-grey);
    line-height: 1;
  }
  .contact-list {
    position: absolute;
    left: 0; right: 0;
    top: 189px;
    list-style: none;
    font-weight: 300;
    font-size: 12.5px;
    line-height: 16.5px;
    color: var(--detail-grey);
  }
</style>
</head>
<body>
  <main class="canvas">
    <section class="card card--front">
      <p class="brand-name">Marla T</p>
      <p class="tagline">CALM STRENGTH EVERY DAY</p>
    </section>

    <section class="card card--back">
      <p class="brand-name">Marla T</p>
      <p class="tagline">CALM STRENGTH EVERY DAY</p>
      <p class="person-name">MARLA TEVENY</p>
      <ul class="contact-list">
        <li>Email: hello@marlatwell.example</li>
        <li>Website: marlatwell.example</li>
        <li>Phone: +610497258316</li>
      </ul>
    </section>
  </main>
</body>
</html>
```